Web Infographic Series

We need a series of 4 infographics to highlight the major findings of a recent report our company published called the "Complete Staff Relocation Survey Study".

We plan to use these infographics on web pages, in social media, and other channels to promote the survey and generate interest in what our company does.

The phrase "Complete Staff Relocation" is a registered tradfemark of Valbrecht Global, so we actually mark it with the (R). We have a tight timeline but WE KNOW YOU CAN DO IT! We have thrown together rough mock ups of the information we want and some of the images that we need to comply with our brand standard to help you.

A overview document of what we want to communicate in the graphics is attached!!
Updates

Please see updated brief!  It will give you the data points and info you need to get started.  Thanks!

Target Market(s)

WE are a B2B company and our target audience is finance executives, HR executives and purchasing/procurement executives. visit www.valbrecht-example.com to get a sense of our "look and feel".

Industry/Entity Type

It Company

Requirements
Must have
• The Valbrecht Global "80th anniversary logo", a (R) after the first mention of the phrase "Complete Staff Relocation", Color scheme of red gradient to dark red with gray, white and accent colors or images (i.e. R 169 G 31 B 35 to a dark red 80 22 16) Must be high impact and fit in with the style of the graphics we have done before see some examples on https://www.valbrecht-example.com/Solutions/Fleet-Auto-Services/Weigh-Your-Fleet-Auto-Plan-Choices.aspx .. and the cover of the report.....we are open to new interpretations of improvements of course!
Nice to have
• we have a set of "mobility" icons attached below. we would like to see them incorporated in the design as well as an image of the cover of the report.
Should not have
• A dark (black) color scheme. Too much color. a cartoon-ish look

```html
<!DOCTYPE html>
<html lang="en">
<head>
<meta charset="utf-8">
<title>2012 Complete Staff Relocation Survey Study</title>
<link href="https://fonts.googleapis.com/css2?family=Libre+Baskerville&family=Arimo:wght@400;700&display=swap" rel="stylesheet">
<style>
:root{
  --red:#a91f23;
  --red-dark:#501610;
  --red-mid:#8c1a1d;
  --gray-band:#e4e4e4;
  --page:#f6f6f6;
  --ink:#333;
  --rule:#dcdcdc;
  --white:#fff;
  --blue:#3b7fc4;
}
*{box-sizing:border-box;margin:0;padding:0}
html,body{width:720px;height:1200px;overflow:hidden}
body{background:var(--page);font-family:"Arimo",Arial,sans-serif;color:var(--ink);position:relative}
.serif{font-family:"Libre Baskerville",Georgia,serif}
.abs{position:absolute}

.top-band{left:0;top:0;width:720px;height:68px;background:linear-gradient(90deg,var(--red),var(--red-mid))}
.gray-band{left:0;top:68px;width:720px;height:148px;background:var(--gray-band)}
.brand-panel{left:108px;top:0;width:137px;height:196px;background:var(--white);clip-path:polygon(0 0,100% 0,100% 84%,88% 100%,0 100%)}
.brand{position:absolute;left:0;top:44px;width:137px;text-align:center}
.brand-dot{display:block;width:22px;height:22px;border-radius:50%;background:var(--red);margin:0 auto 8px}
.brand-name{font-family:"Libre Baskerville",Georgia,serif;font-size:12px;color:var(--red)}
.brand-copy{position:absolute;left:15px;top:126px;width:115px;font-size:6.6px;line-height:9.6px;color:#555}

.title{left:270px;top:18px;color:var(--white)}
.title h1{font-family:"Libre Baskerville",Georgia,serif;font-weight:400;font-size:19px;line-height:22px}
.title p{font-family:"Libre Baskerville",Georgia,serif;font-size:9.6px;line-height:10px}
.icons{left:276px;top:98px;width:330px;height:56px}
.tagline{left:276px;top:163px;font-family:"Libre Baskerville",Georgia,serif;font-size:13.6px;color:var(--red)}

.section-title{display:flex;align-items:center;gap:6px;font-family:"Libre Baskerville",Georgia,serif;font-size:10.4px;color:#555}
.section-title .tag{color:var(--red)}
.section-title .num{color:var(--red);font-size:13px}
.facts{list-style:none}
.facts li{position:relative;padding:5px 0 6px 9px;border-bottom:1px solid var(--rule);font-size:6.6px;line-height:9.6px;color:#444}
.facts li:last-child{border-bottom:none}
.facts li::before{content:"›";position:absolute;left:0;top:3px;color:var(--red);font-size:10px;line-height:10px}

.art{border-radius:6px}
.footer{left:0;top:1072px;width:720px;height:76px;background:linear-gradient(180deg,var(--red),var(--red-mid))}
.footer-base{left:0;top:1148px;width:720px;height:52px;background:linear-gradient(180deg,#7a1c19,var(--red-dark))}
.cover{left:108px;top:1064px;width:64px;height:84px;background:linear-gradient(180deg,#fafafa,#ececec 70%,var(--red) 70%);box-shadow:0 1px 3px rgba(0,0,0,.3)}
.cta{left:172px;top:1086px;width:476px;text-align:center;color:var(--white);font-family:"Libre Baskerville",Georgia,serif;font-size:10.4px;line-height:13.6px}
.cta strong{font-weight:700}
.legal{left:0;top:1162px;width:720px;text-align:center;color:var(--white);font-size:6.4px;line-height:9.6px}
</style>
</head>
<body>

<div class="abs top-band"></div>
<div class="abs gray-band"></div>

<div class="abs brand-panel">
  <div class="brand"><span class="brand-dot"></span><span class="brand-name">Valbrecht Global</span></div>
  <p class="brand-copy">We help organizations increase agility, reduce costs, and improve satisfaction through innovative employee mobility management services</p>
</div>

<div class="abs title">
  <h1>2012 Complete Staff Relocation</h1>
  <p>Survey Study</p>
</div>

<svg class="abs icons" viewBox="0 0 330 56" fill="#a91f23" aria-hidden="true">
  <!-- row one -->
  <path d="M0 12h22l-2 2H4z M9 3l3 0 4 9h-4z M9 21l3 0 4-9h-4z M2 8h2l1 4H3z"/>
  <rect x="62" y="8" width="22" height="7" rx="3"/><path d="M66 8l3-4h8l3 4z"/><circle cx="67" cy="16" r="2.5"/><circle cx="79" cy="16" r="2.5"/>
  <circle cx="136" cy="10" r="9"/><path d="M131 6h5l2 4-4 4z" fill="#fff"/>
  <rect x="188" y="1" width="12" height="19" rx="2" fill="none" stroke="#a91f23" stroke-width="2"/>
  <rect x="246" y="3" width="12" height="15" rx="1" fill="none" stroke="#a91f23" stroke-width="2"/><path d="M256 2l4 4-8 8-3 1 1-3z"/>
  <path d="M305 4a5 5 0 0 1 10 0c0 4-5 9-5 9s-5-5-5-9z"/><rect x="301" y="12" width="16" height="8"/>
  <!-- row two -->
  <path d="M2 44l9-9 9 9h-3v8h-12v-8z"/>
  <path d="M64 48h22v4H64z M68 47v-5h14v5z M70 42l5-3 5 3z"/>
  <path d="M126 42l10-5 10 5z M127 43h18v2h-18z M129 46h2v5h-2z M134 46h2v5h-2z M139 46h2v5h-2z M127 51h18v2h-18z"/>
  <rect x="188" y="38" width="16" height="13" rx="2"/><path d="M193 38v-3h6v3" fill="none" stroke="#a91f23" stroke-width="1.5"/><path d="M195 41h2v3h3v2h-3v3h-2v-3h-3v-2h3z" fill="#fff"/>
  <rect x="246" y="37" width="18" height="13" rx="2"/><rect x="246" y="40" width="18" height="2.5" fill="#fff"/>
  <rect x="300" y="36" width="16" height="4"/><rect x="300" y="42" width="16" height="4"/><rect x="300" y="48" width="16" height="4"/>
</svg>

<div class="abs tagline">Growing organizations are investing in mobility</div>

<!-- Section 1 -->
<div class="abs" style="left:108px;top:240px;width:230px">
  <h2 class="section-title"><svg width="24" height="24" viewBox="0 0 24 24" aria-hidden="true"><circle cx="12" cy="12" r="12" fill="#a91f23"/><path d="M6 8h6l2 4-4 5-2-3z" fill="#fff" opacity=".8"/></svg><span class="tag">Graphic -<span class="num">1</span>-</span> TEM Overall Key Findings:</h2>
  <ul class="facts" style="margin-top:8px">
    <li>30% of the workforce is mobile – which means they travel, drive vehicles, or relocate for business /70% non-mobile</li>
    <li>Companies with mobility programs have higher productivity. An average of 85% reported that they saw improved employee productivity after implementing a defined mobility program.</li>
    <li>Growing organizations are investing in mobility. Companies with 10% or more annual growth in revenue have more mobile employees than companies with low growth.</li>
    <li>Mobility differences between high-growth and low-growth companies: growth organizations invest average of $11,779/mobile employee and non-growth organizations only invest an average of $6,527/mobile employee</li>
  </ul>
</div>

<svg class="abs" style="left:366px;top:260px" width="244" height="150" viewBox="0 0 244 150" font-family="Arimo,Arial,sans-serif" font-size="6" fill="#444" role="img" aria-label="Line chart: respondents who implemented versus respondents reporting improved productivity">
  <line x1="0" y1="6" x2="8" y2="6" stroke="#3b7fc4" stroke-width="1.5"/><text x="11" y="8">Respondents who Implemented</text>
  <line x1="103" y1="6" x2="111" y2="6" stroke="#a91f23" stroke-width="1.5"/><text x="114" y="8">Respondents Reporting Improved Productivity</text>
  <polyline points="0,45 10,45 50,44 94,38 134,41 174,43 222,42 242,41" fill="none" stroke="#a91f23" stroke-width="1.5"/>
  <polyline points="0,66 10,66 50,66 94,65 134,64 174,56 222,54 242,53" fill="none" stroke="#3b7fc4" stroke-width="1.5"/>
  <text x="4" y="38">81%</text><text x="46" y="37">83%</text><text x="88" y="32">96%</text><text x="129" y="35">87%</text><text x="169" y="37">82%</text><text x="215" y="36">87%</text>
  <text x="4" y="61">21%</text><text x="46" y="61">23%</text><text x="88" y="61">25%</text><text x="129" y="59">30%</text><text x="169" y="51">48%</text><text x="215" y="49">54%</text>
  <line x1="0" y1="86" x2="242" y2="86" stroke="#ccc"/>
  <g stroke="#ccc"><line x1="30" y1="86" x2="30" y2="140"/><line x1="72" y1="86" x2="72" y2="140"/><line x1="114" y1="86" x2="114" y2="140"/><line x1="154" y1="86" x2="154" y2="140"/><line x1="196" y1="86" x2="196" y2="140"/></g>
  <g font-size="5.6">
    <text transform="translate(12,148) rotate(-90)">Company Vechicles</text>
    <text transform="translate(50,128) rotate(-90)">Relocation</text><text transform="translate(56,128) rotate(-90)">Program</text>
    <text transform="translate(92,132) rotate(-90)">Expense Mgmt.</text><text transform="translate(98,132) rotate(-90)">Software</text>
    <text transform="translate(132,142) rotate(-90)">Tools/Software/Ap</text><text transform="translate(138,142) rotate(-90)">ps for Mobile</text>
    <text transform="translate(172,138) rotate(-90)">Personal Vechile</text><text transform="translate(178,138) rotate(-90)">Reimbursement</text><text transform="translate(184,138) rotate(-90)">program</text>
    <text transform="translate(224,132) rotate(-90)">Mobilr Devices</text>
  </g>
</svg>

<!-- Section 2 -->
<div class="abs art" style="left:120px;top:456px;width:160px;height:112px;background:radial-gradient(ellipse at center,#e4e4e4,#f4f4f4 70%)" role="img" aria-label="Illustration of a white passenger airplane"></div>
<div class="abs" style="left:368px;top:460px;width:232px">
  <h2 class="section-title"><svg width="26" height="22" viewBox="0 0 26 22" aria-hidden="true"><path d="M0 11h26l-3 2H4z M10 0h3l5 11h-5z M10 22h3l5-11h-5z M1 6h2l2 5H3z" fill="#a91f23"/></svg><span class="tag">Graphic -<span class="num">2</span>-</span> Travel:</h2>
  <ul class="facts" style="margin-top:6px">
    <li>Direct Spend/traveler is $10,997</li>
    <li>Support cost/traveler is $713</li>
    <li>Support costs as percentage of direct spend is 10%</li>
    <li>Participants with expense management software spent $2775 less per traveler per year than companies using paper based reporting.</li>
  </ul>
</div>

<!-- Section 3 -->
<div class="abs" style="left:108px;top:632px;width:232px">
  <h2 class="section-title"><svg width="30" height="14" viewBox="0 0 30 14" aria-hidden="true"><rect x="0" y="5" width="30" height="6" rx="3" fill="#a91f23"/><path d="M6 5l4-5h10l4 5z" fill="#a91f23"/><circle cx="7" cy="11" r="3" fill="#a91f23" stroke="#fff"/><circle cx="23" cy="11" r="3" fill="#a91f23" stroke="#fff"/></svg><span class="tag">Graphic -<span class="num">3</span>-</span> Business Vehicles:</h2>
  <ul class="facts" style="margin-top:6px">
    <li>Average direct spend/driver is $8710</li>
    <li>Support cost/driver is $699</li>
    <li>Support costs as percentage of direct spend is 9.5%</li>
    <li>High growth companies have greater efficiency: high growth: one full-time support person can support 731 business drivers,in a low growth organization 1 FTE supports only 458. This could be explained by the fact that high-growth organizations invest more in their mobile programs.</li>
    <li>Graphic to show direct spend per driver…($10,808 for fleet programs vs. $8120 for reimbursement programs)</li>
  </ul>
</div>
<div class="abs art" style="left:384px;top:632px;width:190px;height:164px;background:linear-gradient(160deg,#e8e8e8,#c9c9c9 60%,#b5b5b5)" role="img" aria-label="Group of business vehicles: vans, trucks and a sedan"></div>

<!-- Section 4 -->
<div class="abs art" style="left:108px;top:860px;width:232px;height:156px;background:linear-gradient(160deg,#d6d6d6,#9a9a9a 55%,#5e5e5e)" role="img" aria-label="Tablets and smartphones grouped together"></div>
<div class="abs" style="left:366px;top:844px;width:234px">
  <h2 class="section-title"><svg width="18" height="22" viewBox="0 0 18 22" aria-hidden="true"><rect x="1.5" y="1.5" width="15" height="19" rx="3" fill="none" stroke="#a91f23" stroke-width="2.5"/></svg><span class="tag">Graphic -<span class="num">4</span>-</span> Mobile Devices:</h2>
  <ul class="facts" style="margin-top:8px">
    <li>Average direct spend/mobile device $1225</li>
    <li>Average support cost/mobile device $211</li>
    <li>Support cost as percentage of direct spend 23%</li>
    <li>30% of companies expect a decrease in company provided mobile device yet 64% of companies do not have an active mobile device policy and 67% do not outsource their programs….the meaning behind that is that the companies have more employees BYOD (bring your own device), they don't have policies in place to manage it and only 27% outsource….if they outsource, they would have a policy and they would be able to get their arms around cost containment and efficiency.</li>
  </ul>
</div>

<!-- Footer -->
<div class="abs footer"></div>
<div class="abs footer-base"></div>
<div class="abs cover" role="img" aria-label="Cover of the 2012 Complete Staff Relocation Survey Study report"></div>
<p class="abs cta">For the full version of the 2012 Complete Staff Relocation Survey Study or to learn more about how Valbrecht Global can help your business optimize your mobile workforce,<br><strong>contact us at info@valbrecht-example.com</strong></p>
<p class="abs legal">Would you like to see how your company stacks up against others in your industry? REGISTER for Valbrecht Global's 2013 Complete Staff Relocation Survey.<br>Copyright © 2013. All right Reserved</p>

</body>
</html>
```